New Labels for VANTO Sports Drinks

Sports drink company looking for new fresh look with commercial appeal beverage labels. You can use the current label as a guide but adjust where you see fit. Would like to standout from other sports drink on store shelves. VANTO Sports Drinks is a fusion of real brewed tea and all natural electrolytes. Our tea features a bold, full-bodied flavor profile, combined with all natural electrolytes, giving you one of the very first tea based sports drinks.

Target Market(s)

16-40

Colors

Designer to choose colors to be used in the design.

Requirements
Must have
• Name
• flavor
• description
• nutritional info
• all Info on back of labels
Nice to have
• sports image
• fruit flavor
• white background
• Real tea and natural electrolytes
Should not have
• n/a

```html
<!DOCTYPE html>
<html lang="en">
<head>
<meta charset="utf-8">
<title>VANTO Sports Tea Labels</title>
<link href="https://fonts.googleapis.com/css2?family=Oswald:wght@300;500;700&display=swap" rel="stylesheet">
<style>
  :root {
    --paper: #ffffff;
    --ink: #0b0b0b;
    --white: #ffffff;
    --red: #e3222c;
    --red-deep: #8e1a20;
    --yellow: #fbec24;
    --yellow-deep: #8c8530;
    --grey-light: #a9a9a9;
    --grey-dark: #2a2a2a;
  }
  * { box-sizing: border-box; margin: 0; padding: 0; }
  html, body {
    width: 1200px;
    height: 1135px;
    overflow: hidden;
    background: var(--paper);
    font-family: "Oswald", "Arial Narrow", sans-serif;
  }
  .label-set {
    position: relative;
    width: 1200px;
    height: 1135px;
  }
  .label {
    position: absolute;
    top: 212px;
    width: 420px;
    height: 710px;
    overflow: hidden;
    background: var(--ink);
  }
  .label--black-tea { left: 150px; --accent: var(--red); --accent-deep: var(--red-deep); --flavor-ink: var(--white); --band-ink: var(--white); }
  .label--lemon { left: 630px; --accent: var(--yellow); --accent-deep: var(--yellow-deep); --flavor-ink: var(--yellow); --band-ink: var(--yellow); }

  .label__color-field {
    position: absolute;
    left: 0; top: 0;
    width: 226px; height: 100%;
    background: var(--accent);
  }
  .label__athlete { position: absolute; }
  .label__athlete--cyclist {
    left: 0; top: 26px;
    width: 226px; height: 630px;
    background: linear-gradient(160deg, var(--accent-deep) 0%, var(--accent-deep) 40%, var(--accent) 95%);
    opacity: 0.8;
  }
  .label__athlete--runner {
    left: 226px; top: 26px;
    width: 194px; height: 684px;
    background: linear-gradient(180deg, var(--grey-light) 0%, var(--grey-dark) 70%, var(--ink) 100%);
    opacity: 0.8;
  }
  .label__divider {
    position: absolute;
    left: 206px;
    width: 20px;
    background: var(--white);
  }
  .label__divider--top { top: 0; height: 96px; }
  .label__divider--upper { top: 166px; height: 92px; }
  .label__divider--middle { top: 400px; height: 125px; }
  .label__divider--bottom { top: 700px; height: 10px; }

  .label__flavor {
    position: absolute;
    left: 0; right: 0; top: 108px;
    text-align: center;
    font-weight: 700;
    font-size: 46px;
    letter-spacing: 0.5px;
    color: var(--flavor-ink);
    line-height: 1;
  }
  .label__brand {
    position: absolute;
    left: 0; right: 0; top: 270px;
    display: flex;
    align-items: center;
    justify-content: center;
    gap: 14px;
  }
  .label__brand-mark {
    width: 26px; height: 26px;
    border-radius: 50%;
    background: var(--white);
  }
  .label__brand-name {
    font-weight: 700;
    font-size: 118px;
    line-height: 1;
    color: var(--white);
  }
  .label__product {
    position: absolute;
    left: 86px; top: 535px;
    display: flex;
    align-items: baseline;
    line-height: 1;
  }
  .label__product-tea {
    width: 128px;
    font-weight: 300;
    font-size: 46px;
    letter-spacing: 6px;
    color: var(--white);
  }
  .label__product-extra {
    font-weight: 700;
    font-size: 28px;
    color: var(--accent);
  }
  .label__band {
    position: absolute;
    left: 60px; top: 598px;
    width: 380px; height: 44px;
    background: var(--ink);
    clip-path: polygon(22px 0, 100% 0, 100% 100%, 0 100%);
    border-top: 4px solid var(--accent);
    display: flex;
    align-items: center;
    padding-left: 40px;
    font-weight: 500;
    font-size: 24px;
    letter-spacing: 10px;
    color: var(--band-ink);
  }
  .label__volume {
    position: absolute;
    left: 96px; right: 60px; top: 670px;
    display: flex;
    justify-content: space-between;
    font-weight: 500;
    font-size: 24px;
    color: var(--white);
    line-height: 1;
  }
</style>
</head>
<body>
<main class="label-set">

  <section class="label label--black-tea">
    <div class="label__color-field"></div>
    <div class="label__athlete label__athlete--cyclist" role="img" aria-label="Red-tinted photo of a mountain biker in a helmet riding toward the viewer"></div>
    <div class="label__athlete label__athlete--runner" role="img" aria-label="Black and white photo of a female runner in a sports top"></div>
    <div class="label__divider label__divider--top"></div>
    <div class="label__divider label__divider--upper"></div>
    <div class="label__divider label__divider--middle"></div>
    <div class="label__divider label__divider--bottom"></div>
    <h2 class="label__flavor">BLACK TEA</h2>
    <div class="label__brand">
      <span class="label__brand-name">VANTO</span>
      <span class="label__brand-mark"></span>
    </div>
    <p class="label__product"><span class="label__product-tea">TEA</span><span class="label__product-extra">+ELECTROLYTES</span></p>
    <p class="label__band">SPORTS TEA</p>
    <p class="label__volume"><span>16 fl.oz.</span><span>(474ml)</span></p>
  </section>

  <section class="label label--lemon">
    <div class="label__color-field"></div>
    <div class="label__athlete label__athlete--cyclist" role="img" aria-label="Yellow-tinted photo of a mountain biker in a helmet riding toward the viewer"></div>
    <div class="label__athlete label__athlete--runner" role="img" aria-label="Black and white photo of a female runner in a sports top"></div>
    <div class="label__divider label__divider--top"></div>
    <div class="label__divider label__divider--upper"></div>
    <div class="label__divider label__divider--middle"></div>
    <div class="label__divider label__divider--bottom"></div>
    <h2 class="label__flavor">LEMON</h2>
    <div class="label__brand">
      <span class="label__brand-name">VANTO</span>
      <span class="label__brand-mark"></span>
    </div>
    <p class="label__product"><span class="label__product-tea">TEA</span><span class="label__product-extra">+ELECTROLYTES</span></p>
    <p class="label__band">SPORTS TEA</p>
    <p class="label__volume"><span>16 fl.oz.</span><span>(474ml)</span></p>
  </section>

</main>
</body>
</html>
```